Celebrity and Entertainment News Website Needed

Entertainment is one of the favors of Life and I am seeking a standard celebrity website which will discuss in depth news of different celebrities around globe with major focus on American Entertainers. There will be different categories of news from these regions. America, Europe, Asia, Australia and Africa. My website name is quorvella. Youthful colors should be used for the theme and designs, Users should be able to comment at the bottom of each news. Glossy pictures of well know celebrities should be used. Designers can get knowledge from http://tuvrapix.com

Industry/Entity Type

Entertainment

Coding

Coded - Design and coding required

```html
<!DOCTYPE html>
<html lang="en">
<head>
<meta charset="utf-8">
<title>Quorvella — Celebrity &amp; Entertainment News</title>
<link href="https://fonts.googleapis.com/css2?family=Bitter:wght@700;800&family=Open+Sans:wght@400;600;700&display=swap" rel="stylesheet">
<style>
:root{
  --navy:#1b2b47;
  --navy-deep:#101b2f;
  --ink:#0f2340;
  --text:#555b66;
  --muted:#8a919c;
  --light:#f1f2f4;
  --white:#ffffff;
  --rule:#dcdfe4;
  --red:#e8412c;
  --green:#7dc242;
  --orange:#f15a24;
  --button:#0e2f66;
  --tag-awards:#e4157f;
  --tag-fashion:#1d9fe0;
  --tag-party:#f3a01b;
  --tag-photos:#2bb35b;
  --title:"Bitter",Georgia,serif;
  --body:"Open Sans",Arial,sans-serif;
}
*{margin:0;padding:0;box-sizing:border-box}
html,body{width:1200px;height:4063px;overflow:hidden}
body{font-family:var(--body);color:var(--text);background:var(--white);position:relative}
.abs{position:absolute}
.photo{position:absolute;display:block}
.g1{background:linear-gradient(135deg,#4b3a36,#9a6b4f 45%,#2a2c3a)}
.g2{background:linear-gradient(135deg,#c9a25a,#6a4a32 55%,#2a2022)}
.g3{background:linear-gradient(135deg,#3d4656,#7a8190 50%,#1e2330)}
.g4{background:linear-gradient(135deg,#c23a2d,#6b2a2a 50%,#222)}
.g5{background:linear-gradient(135deg,#1e2a3a,#5a6b80 50%,#a89a88)}
.g6{background:linear-gradient(135deg,#e6c07a,#a8683a 50%,#3a2a22)}
.g7{background:linear-gradient(135deg,#2f6e7d,#9fb7bd 50%,#39424d)}
.g8{background:linear-gradient(135deg,#6d2f2a,#c28a6b 50%,#2c3238)}

/* header */
.masthead{position:absolute;left:0;top:0;width:1200px;height:542px;background:var(--navy)}
.topbar{position:absolute;left:200px;top:22px;width:802px;height:24px;font-size:12px;color:#c9d0db;display:flex;align-items:center}
.topbar .social{display:flex;gap:6px;margin-left:10px}
.dot{width:20px;height:20px;border-radius:50%;background:#2d4066;border:1px solid #3f5580}
.topbar .tools{margin-left:auto;display:flex;gap:18px;align-items:center}
.brand{position:absolute;left:200px;top:66px;font-family:var(--title);font-weight:800;font-size:32px;color:var(--white)}
.nav{position:absolute;right:198px;top:74px;display:flex;gap:18px;font-size:12.5px;color:#d5dbe5}
.nav a{color:inherit;text-decoration:none;position:relative;padding-bottom:8px}
.nav a.active{color:var(--white)}
.nav a.active::after{content:"";position:absolute;left:0;right:0;bottom:0;height:3px;background:var(--red)}
.ad{position:absolute;left:328px;top:135px;width:547px;height:66px;background:var(--orange);display:flex;align-items:center}
.ad .ad-brand{width:110px;height:100%;background:var(--white);color:var(--orange);font-weight:700;font-size:15px;display:flex;align-items:center;justify-content:center}
.ad .ad-copy{flex:1;color:var(--white);text-align:center;font-size:17px;font-weight:700;line-height:1.2}
.ad .ad-copy small{display:block;font-size:13px;font-weight:600}
.ad .ad-cta{width:96px;height:34px;margin-right:14px;background:var(--white);color:var(--orange);font-size:10px;font-weight:700;display:flex;align-items:center;justify-content:center;text-align:center;line-height:1.1}
.regions{position:absolute;left:0;width:1200px;top:240px;display:flex;justify-content:center;gap:20px;font-family:var(--title);font-weight:700;font-size:17px;color:var(--white);align-items:center}
.regions span{display:flex;align-items:center;gap:10px}
.regions i{width:26px;height:22px;background:#e6eaf0;border-radius:5px;display:inline-block}
.regions .on{color:var(--green)}
.regions .sep{width:2px;height:22px;background:#ffffff80}

/* hero */
.hero-main{left:200px;top:298px;width:531px;height:398px}
.hero-side1{left:737px;top:298px;width:265px;height:195px}
.hero-side2{left:737px;top:499px;width:265px;height:197px}
.hero-cap{position:absolute;color:var(--white)}
.hero-cap b{display:block;font-weight:700}
.hero-main .hero-cap{left:22px;bottom:22px;font-size:13px}
.hero-main .hero-cap b{font-size:17px;margin-bottom:6px}
.hero-side1 .hero-cap,.hero-side2 .hero-cap{left:22px;bottom:14px;font-size:11px;width:210px}
.hero-cap b{font-size:12px}
.pager{position:absolute;right:14px;top:14px;display:flex;gap:6px}
.pager i{width:8px;height:8px;border-radius:50%;background:#ffffff80}
.pager i:first-child{background:var(--white)}

/* sections */
.band-light{position:absolute;left:0;top:542px;width:1200px;height:466px;background:var(--light)}
.sec-title{position:absolute;left:0;width:1200px;text-align:center;font-family:var(--title);font-weight:700;font-size:27px;color:var(--ink)}
.sec-rule{position:absolute;left:200px;width:802px;height:5px;background:var(--rule)}
.date{font-weight:700;color:var(--ink);font-size:11px;display:block;margin-bottom:6px}
.blurb{font-size:10.5px;line-height:1.45;color:var(--text)}
.recent-item{position:absolute;top:772px;width:152px}
.recent-item .photo{position:relative;width:152px;height:117px}
.recent-item .txt{margin-top:20px}

/* featured */
.tag{position:absolute;left:10px;top:26px;color:var(--white);font-family:var(--title);font-weight:700;font-size:15px;padding:7px 14px}
.feat{position:absolute}
.feat .txt{position:absolute;left:0;width:100%}
.button{position:absolute;left:200px;top:1731px;width:802px;height:68px;background:var(--button);color:var(--white);font-family:var(--title);font-weight:700;font-size:17px;display:flex;align-items:center;justify-content:center}

/* celebrities */
.band-dark{position:absolute;left:0;top:1858px;width:1200px;height:493px;background:linear-gradient(180deg,#16223a,#0d1627)}
.band-dark .sec-title{color:var(--white)}
.celeb{position:absolute;top:1997px;width:260px}
.celeb .photo{position:relative;width:100%;height:151px}
.celeb .date{color:var(--white);margin-top:18px}
.celeb .blurb{color:#aeb6c3}
.shares{display:flex;gap:5px;margin-top:14px}
.shares i{width:16px;height:16px;border-radius:50%;border:1px solid #9aa3b0}
.arrow{position:absolute;top:2110px;width:14px;height:14px}

/* videos */
.play{position:absolute;left:50%;top:50%;transform:translate(-50%,-50%)}

/* hot news */
.col-title{position:absolute;font-family:var(--title);font-weight:700;font-size:27px;color:var(--ink)}
.col-arrows{position:absolute;display:flex;gap:8px}
.hot{position:absolute;width:255px}
.hot .photo{position:relative;width:100%;height:154px}
.hot .date{margin-top:20px}
.list-item{position:absolute;left:745px;width:257px;border-bottom:2px dashed var(--rule);padding-bottom:12px}

/* strip + footer */
.strip{position:absolute;top:3595px;height:211px;width:300px}
.strip .icons{position:absolute;right:34px;top:62px;display:flex;flex-direction:column;gap:8px}
.strip .icons i{width:12px;height:12px;border-radius:50%;background:#e8ecf2}
.footer{position:absolute;left:0;top:3806px;width:1200px;height:257px;background:var(--navy-deep);color:#c9d0db;font-size:11px}
.footer .brand{position:static;text-align:center;padding-top:56px;font-size:30px}
.foot-row{position:absolute;top:108px;left:0;width:1200px;display:flex;justify-content:center;align-items:center;gap:10px}
.foot-row .dot{width:18px;height:18px}
.newsletter{display:flex;align-items:center;gap:8px;margin-left:80px}
.newsletter .field{width:146px;height:20px;background:#1c2b44;color:#7d8797;font-size:9px;padding:4px 8px}
.newsletter .go{height:20px;background:var(--green);color:var(--white);font-weight:700;font-size:9px;padding:4px 12px}
.foot-nav{position:absolute;top:168px;left:0;width:1200px;display:flex;justify-content:center;gap:14px}
.copy{position:absolute;top:200px;left:0;width:1200px;text-align:center;font-size:10.5px}
</style>
</head>
<body>

<header class="masthead">
  <div class="topbar">
    <span>Connect With Us</span>
    <div class="social"><i class="dot"></i><i class="dot"></i><i class="dot"></i><i class="dot"></i><i class="dot"></i><i class="dot"></i></div>
    <div class="tools">
      <span style="display:flex;gap:6px;align-items:center"><svg width="11" height="11" viewBox="0 0 12 12"><circle cx="5" cy="5" r="4" fill="none" stroke="#c9d0db" stroke-width="1.6"/><line x1="8" y1="8" x2="11" y2="11" stroke="#c9d0db" stroke-width="1.6"/></svg>Search</span>
      <span style="display:flex;gap:6px;align-items:center"><svg width="11" height="11" viewBox="0 0 12 12"><circle cx="6" cy="6" r="5" fill="none" stroke="#c9d0db" stroke-width="1.4"/><path d="M1 6h10M6 1c3 3 3 7 0 10M6 1c-3 3-3 7 0 10" fill="none" stroke="#c9d0db" stroke-width="1"/></svg>Regions</span>
    </div>
  </div>
  <div class="brand">Quorvella</div>
  <nav class="nav">
    <a class="active">Home</a><a>About Us</a><a>Entertainment</a><a>News</a><a>Regions</a><a>Categories</a><a>Faq's</a><a>Contact Us</a>
  </nav>
  <div class="ad">
    <div class="ad-brand">Bannerloft</div>
    <div class="ad-copy">Do you need banners like this one<small>to advertise your company on the internet?</small></div>
    <div class="ad-cta">WE CAN MAKE<br>THEM FOR YOU</div>
  </div>
  <div class="regions">
    <span class="on"><i role="img" aria-label="America map icon"></i>America</span><b class="sep"></b>
    <span><i role="img" aria-label="Europe map icon"></i>Europe</span><b class="sep"></b>
    <span><i role="img" aria-label="Asia map icon"></i>Asia</span><b class="sep"></b>
    <span><i role="img" aria-label="Australia map icon"></i>Australia</span><b class="sep"></b>
    <span><i role="img" aria-label="Africa map icon"></i>Africa</span>
  </div>
</header>

<div class="band-light"></div>

<section>
  <div class="photo hero-main g1" role="img" aria-label="Celebrity in a suit at an evening event">
    <div class="pager"><i></i><i></i><i></i><i></i></div>
    <div class="hero-cap"><b>July 27th 2016</b>Neque porro quisquam est qui dolorem ipsum quia dolor sit amet....</div>
  </div>
  <div class="photo hero-side1 g6" role="img" aria-label="Actress smiling on the red carpet">
    <div class="hero-cap"><b>July 27th 2016</b>Neque porro quisquam est qui dolorem ipsum quia dolor sit amet...</div>
  </div>
  <div class="photo hero-side2 g3" role="img" aria-label="Singer posing at a gala">
    <div class="hero-cap"><b>July 27th 2016</b>Neque porro quisquam est qui dolorem ipsum quia dolor sit amet...</div>
  </div>
</section>

<section>
  <h2 class="sec-title" style="top:714px">Recent News</h2>
  <article class="recent-item" style="left:200px"><div class="photo g5" role="img" aria-label="Couple at a premiere"></div><div class="txt"><span class="date">July 27th 2016</span><p class="blurb">Neque porro quisquam est qui dolorem ipsum quia dolor...</p></div></article>
  <article class="recent-item" style="left:362px"><div class="photo g6" role="img" aria-label="Performer on stage"></div><div class="txt"><span class="date">July 27th 2016</span><p class="blurb">Neque porro quisquam est qui dolorem ipsum quia dolor...</p></div></article>
  <article class="recent-item" style="left:525px"><div class="photo g8" role="img" aria-label="Two public figures at an event"></div><div class="txt"><span class="date">July 27th 2016</span><p class="blurb">Neque porro quisquam est qui dolorem ipsum quia dolor...</p></div></article>
  <article class="recent-item" style="left:687px"><div class="photo g1" role="img" aria-label="Star at an awards night"></div><div class="txt"><span class="date">July 27th 2016</span><p class="blurb">Neque porro quisquam est qui dolorem ipsum quia dolor...</p></div></article>
  <article class="recent-item" style="left:850px"><div class="photo g3" role="img" aria-label="Red carpet with photographers"></div><div class="txt"><span class="date">July 27th 2016</span><p class="blurb">Neque porro quisquam est qui dolorem ipsum quia dolor...</p></div></article>
</section>

<section>
  <h2 class="sec-title" style="top:1055px">Featured News</h2>
  <div class="sec-rule" style="top:1108px"></div>

  <article class="feat" style="left:200px;top:1146px;width:252px">
    <div class="photo g2" style="position:relative;width:252px;height:466px" role="img" aria-label="Actor holding an award trophy"><span class="tag" style="background:var(--tag-awards)">Awards</span></div>
    <div style="margin-top:14px"><span class="date">July 27th 2016</span><p class="blurb">Lorem Ipsum is simply dummy text of the printing and typesetting industry. Lorem Ipsum has been the industry's standard dummy text ever since the 1500s.</p></div>
  </article>
  <article class="feat" style="left:463px;top:1146px;width:263px">
    <div class="photo g7" style="position:relative;width:263px;height:187px" role="img" aria-label="Model at a fashion event"><span class="tag" style="background:var(--tag-fashion)">Fashion</span></div>
    <div style="margin-top:14px"><span class="date">July 27th 2016</span><p class="blurb">Lorem Ipsum is simply dummy text of the printing and typesetting industry. Lorem Ipsum has been the industry's standard dummy text ever since the 1500s.</p></div>
  </article>
  <article class="feat" style="left:736px;top:1146px;width:266px">
    <div class="photo g6" style="position:relative;width:266px;height:187px" role="img" aria-label="Guests at a glamorous party"><span class="tag" style="background:var(--tag-party)">Party</span></div>
    <div style="margin-top:14px"><span class="date">July 27th 2016</span><p class="blurb">Lorem Ipsum is simply dummy text of the printing and typesetting industry. Lorem Ipsum has been the industry's standard dummy text ever since the 1500s.</p></div>
  </article>
  <article class="feat" style="left:463px;top:1422px;width:263px">
    <div class="photo g5" style="position:relative;width:263px;height:190px" role="img" aria-label="Portrait of an actress"><span class="tag" style="background:var(--tag-photos)">Photos</span></div>
    <div style="margin-top:14px"><span class="date">July 27th 2016</span><p class="blurb">Lorem Ipsum is simply dummy text of the printing and typesetting industry. Lorem Ipsum has been the industry's standard dummy text ever since the 1500s.</p></div>
  </article>
  <article class="feat" style="left:736px;top:1422px;width:266px">
    <div class="photo g4" style="position:relative;width:266px;height:190px" role="img" aria-label="Portrait of an artist in a striped shirt"><span class="tag" style="background:var(--tag-photos)">Photos</span></div>
    <div style="margin-top:14px"><span class="date">July 27th 2016</span><p class="blurb">Lorem Ipsum is simply dummy text of the printing and typesetting industry. Lorem Ipsum has been the industry's standard dummy text ever since the 1500s.</p></div>
  </article>

  <div class="button">View More News</div>
</section>

<section class="band-dark">
  <h2 class="sec-title" style="top:40px">Top Celebrities</h2>
</section>
<svg class="arrow" style="left:143px" viewBox="0 0 14 14"><path d="M9 2 4 7l5 5" fill="none" stroke="#fff" stroke-width="2"/></svg>
<svg class="arrow" style="left:1043px" viewBox="0 0 14 14"><path d="M5 2l5 5-5 5" fill="none" stroke="#fff" stroke-width="2"/></svg>
<article class="celeb" style="left:200px;width:266px"><div class="photo g3" role="img" aria-label="Actor in sunglasses"></div><span class="date">July 27th 2016</span><p class="blurb">Lorem Ipsum is simply dummy text of the printing and typesetting industry. Lorem Ipsum has been the industry's standard dummy text ever since the 1500s.</p><div class="shares"><i></i><i></i><i></i><i></i><i></i><i></i></div></article>
<article class="celeb" style="left:477px;width:255px"><div class="photo g4" role="img" aria-label="Actor in a dark suit"></div><span class="date">July 27th 2016</span><p class="blurb">Lorem Ipsum is simply dummy text of the printing and typesetting industry. Lorem Ipsum has been the industry's standard dummy text ever since the 1500s.</p><div class="shares"><i></i><i></i><i></i><i></i><i></i><i></i></div></article>
<article class="celeb" style="left:750px;width:252px"><div class="photo g7" role="img" aria-label="Actor at an outdoor premiere"></div><span class="date">July 27th 2016</span><p class="blurb">Lorem Ipsum is simply dummy text of the printing and typesetting industry. Lorem Ipsum has been the industry's standard dummy text ever since the 1500s.</p><div class="shares"><i></i><i></i><i></i><i></i><i></i><i></i></div></article>

<section>
  <h2 class="sec-title" style="top:2393px">Videos Of The Week</h2>
  <div class="sec-rule" style="top:2455px"></div>
  <div class="photo g3" style="left:200px;top:2495px;width:472px;height:298px" role="img" aria-label="Video still of a model on the red carpet">
    <svg class="play" width="96" height="96" viewBox="0 0 96 96"><circle cx="48" cy="48" r="46" fill="#111a"/><path d="M38 28l32 20-32 20z" fill="#fff"/></svg>
  </div>
  <div class="photo g8" style="left:680px;top:2495px;width:322px;height:146px" role="img" aria-label="Video still of a celebrity greeting fans">
    <svg class="play" width="44" height="44" viewBox="0 0 96 96"><circle cx="48" cy="48" r="46" fill="#111a"/><path d="M38 28l32 20-32 20z" fill="#fff"/></svg>
  </div>
  <div class="photo" style="left:680px;top:2649px;width:322px;height:144px;background:linear-gradient(135deg,#1a1d24,#3a3f4a)" role="img" aria-label="Video still of an evening premiere">
    <svg class="play" width="44" height="44" viewBox="0 0 96 96"><circle cx="48" cy="48" r="46" fill="#111a"/><path d="M38 28l32 20-32 20z" fill="#fff"/></svg>
  </div>
</section>

<section>
  <h2 class="col-title" style="left:200px;top:2856px">Hot News In Hollywood</h2>
  <div class="col-arrows" style="left:702px;top:2866px"><svg width="12" height="14" viewBox="0 0 12 14"><path d="M8 2 3 7l5 5" fill="none" stroke="#0f2340" stroke-width="2"/></svg><svg width="12" height="14" viewBox="0 0 12 14"><path d="M4 2l5 5-5 5" fill="none" stroke="#0f2340" stroke-width="2"/></svg></div>
  <div class="sec-rule" style="top:2908px;width:526px"></div>

  <article class="hot" style="left:200px;top:2937px"><div class="photo g8" role="img" aria-label="Actress at a press backdrop"></div><span class="date">July 27th 2016</span><p class="blurb">Lorem Ipsum is simply dummy text of the printing and typesetting industry. Lorem Ipsum has been the industry's standard dummy text ever since the 1500s.</p><div class="shares"><i></i><i></i><i></i><i></i><i></i><i></i></div></article>
  <article class="hot" style="left:471px;top:2937px"><div class="photo g6" role="img" aria-label="Stack of celebrity magazines"></div><span class="date">July 27th 2016</span><p class="blurb">Lorem Ipsum is simply dummy text of the printing and typesetting industry. Lorem Ipsum has been the industry's standard dummy text ever since the 1500s.</p><div class="shares"><i></i><i></i><i></i><i></i><i></i><i></i></div></article>
  <article class="hot" style="left:200px;top:3259px"><div class="photo g4" role="img" aria-label="Actor in front of a red backdrop"></div><span class="date">July 27th 2016</span><p class="blurb">Lorem Ipsum is simply dummy text of the printing and typesetting industry. Lorem Ipsum has been the industry's standard dummy text ever since the 1500s.</p><div class="shares"><i></i><i></i><i></i><i></i><i></i><i></i></div></article>
  <article class="hot" style="left:471px;top:3259px"><div class="photo g5" role="img" aria-label="Star wearing a cap and sunglasses"></div><span class="date">July 27th 2016</span><p class="blurb">Lorem Ipsum is simply dummy text of the printing and typesetting industry. Lorem Ipsum has been the industry's standard dummy text ever since the 1500s.</p><div class="shares"><i></i><i></i><i></i><i></i><i></i><i></i></div></article>

  <h2 class="col-title" style="left:745px;top:2856px">Recent News</h2>
  <div class="col-arrows" style="left:972px;top:2866px"><svg width="12" height="14" viewBox="0 0 12 14"><path d="M8 2 3 7l5 5" fill="none" stroke="#0f2340" stroke-width="2"/></svg><svg width="12" height="14" viewBox="0 0 12 14"><path d="M4 2l5 5-5 5" fill="none" stroke="#0f2340" stroke-width="2"/></svg></div>
  <div class="sec-rule" style="left:745px;top:2908px;width:257px"></div>
  <div class="list-item" style="top:2937px"><span class="date">July 27th 2016</span><p class="blurb">Lorem Ipsum is simply dummy text of the printing and typesetting industry. Lorem Ipsum has been the industry's standard dummy text ever since the 1500s.</p></div>
  <div class="list-item" style="top:3043px"><span class="date">July 27th 2016</span><p class="blurb">Lorem Ipsum is simply dummy text of the printing and typesetting industry. Lorem Ipsum has been the industry's standard dummy text ever since the 1500s.</p></div>
  <div class="list-item" style="top:3149px"><span class="date">July 27th 2016</span><p class="blurb">Lorem Ipsum is simply dummy text of the printing and typesetting industry. Lorem Ipsum has been the industry's standard dummy text ever since the 1500s.</p></div>
  <div class="list-item" style="top:3255px"><span class="date">July 27th 2016</span><p class="blurb">Lorem Ipsum is simply dummy text of the printing and typesetting industry. Lorem Ipsum has been the industry's standard dummy text ever since the 1500s.</p></div>
  <div class="list-item" style="top:3361px"><span class="date">July 27th 2016</span><p class="blurb">Lorem Ipsum is simply dummy text of the printing and typesetting industry. Lorem Ipsum has been the industry's standard dummy text ever since the 1500s.</p></div>
  <div class="list-item" style="top:3467px"><span class="date">July 27th 2016</span><p class="blurb">Lorem Ipsum is simply dummy text of the printing and typesetting industry. Lorem Ipsum has been the industry's standard dummy text ever since the 1500s.</p></div>
</section>

<section>
  <div class="strip" style="left:0;background:linear-gradient(135deg,#2a3550,#5a5460 60%,#1a2236)" role="img" aria-label="Celebrity couple at a gala"><div class="icons"><i></i><i></i><i></i><i></i></div></div>
  <div class="strip" style="left:300px;background:linear-gradient(135deg,#1c2a44,#35486a 60%,#141f33)" role="img" aria-label="Singer performing on stage"><div class="icons"><i></i><i></i><i></i><i></i></div></div>
  <div class="strip" style="left:600px;background:linear-gradient(135deg,#2c3650,#4d5670 60%,#182238)" role="img" aria-label="Star posing in an evening dress"><div class="icons"><i></i><i></i><i></i><i></i></div></div>
  <div class="strip" style="left:900px;background:linear-gradient(135deg,#1a2740,#3a4a66 60%,#111b2d)" role="img" aria-label="Crowd at a film festival"><div class="icons"><i></i><i></i><i></i><i></i></div></div>
</section>

<footer class="footer">
  <div class="brand">Quorvella</div>
  <div class="foot-row">
    <span>Connect With Us</span><i class="dot"></i><i class="dot"></i><i class="dot"></i><i class="dot"></i><i class="dot"></i><i class="dot"></i>
    <div class="newsletter"><span>Newsletter Sign Up</span><span class="field">Enter Your E-Mail Address</span><span class="go">SUBSCRIBE NOW</span></div>
  </div>
  <nav class="foot-nav"><span>Home</span><span>About Us</span><span>Entertainment</span><span>News</span><span>Regions</span><span>Categories</span><span>Faq's</span><span>Contact Us</span></nav>
  <p class="copy">© 2016 Company Name &nbsp;|&nbsp; All Rights Reserved</p>
</footer>

</body>
</html>
```